Home Security Company Business Card

Looking for a eye catching business card that is non traditional and stands out but yet still looks professional. It should include all the pertinent information such as name, title, address, telephone, e-mail, website address should definitely stand out and then finally the logo.

Target Market(s)

Residential and Commercial accounts mostly upscale accounts

Industry/Entity Type

Security

Contact Information for Business Card

Name
Title
Address
Office #
Cell #
E-mail
Website

Font styles to use
Serif
Sans Serif

Requirements
Must have
• Logo, two sided color configuration
Nice to have
• You decide
Should not have
• There really aren't any.

```html
<!DOCTYPE html>
<html lang="en">
<head>
<meta charset="utf-8">
<title>Ironvale Home Protection – Business Card</title>
<link rel="stylesheet" href="https://fonts.googleapis.com/css2?family=Lato:wght@400;700&family=Tinos&display=swap">
<style>
  :root{
    --bg:#2b2b2b;
    --card-white:#ffffff;
    --card-shade:#ececec;
    --brand-red:#8e1a12;
    --deep-red:#6e0c07;
    --gold:#e3bf55;
    --gold-light:#f0d27a;
    --ink-grey:#555555;
    --ink-dark:#333333;
    --text-light:#f4eeee;
  }
  *{box-sizing:border-box;margin:0;padding:0}
  html,body{width:1200px;height:997px;overflow:hidden}
  body{background:var(--bg);font-family:"Lato",sans-serif;position:relative}

  .card{position:absolute;left:250px;width:700px;height:400px;overflow:hidden;box-shadow:0 10px 30px rgba(0,0,0,.45)}
  .card--front{top:68px;background:linear-gradient(160deg,var(--card-white) 55%,var(--card-shade))}
  .card--back{top:528px;background:radial-gradient(ellipse at 40% 40%,#7c0d08,var(--deep-red) 70%)}

  .holder{position:absolute;left:60px;top:150px}
  .holder__name{font-weight:700;font-size:22px;color:var(--brand-red);letter-spacing:.5px;text-transform:uppercase}
  .holder__title{font-size:17px;color:var(--ink-grey);margin-top:2px}

  .contact{position:absolute;left:60px;top:222px;list-style:none}
  .contact__row{display:flex;align-items:center;height:30px;margin-bottom:4px}
  .contact__icon{width:26px;height:26px;background:var(--brand-red);display:flex;align-items:center;justify-content:center;margin-right:14px}
  .contact__icon svg{width:16px;height:16px}
  .contact__text{font-size:16px;color:var(--ink-dark)}

  .brand{position:absolute;right:60px;top:120px;display:flex;flex-direction:column;align-items:center;gap:14px}
  .brand__mark{width:86px;height:86px;border-radius:50%;background:var(--brand-red)}
  .brand__name{font-family:"Tinos",serif;font-size:26px;color:var(--brand-red);text-align:center;line-height:1.1;text-transform:uppercase}

  .footer-band{position:absolute;left:0;bottom:0;width:100%;height:56px}
  .footer-band svg{position:absolute;inset:0}
  .footer-band__tagline{position:absolute;left:40px;bottom:14px;font-weight:700;font-size:17px;color:var(--card-white)}
  .footer-band__web{position:absolute;right:28px;bottom:22px;font-weight:700;font-size:16px;color:var(--card-white)}

  .back-name{position:absolute;right:60px;bottom:70px;font-family:"Tinos",serif;color:var(--text-light);text-transform:uppercase;text-align:right;line-height:1.05}
  .back-name__main{font-size:46px}
  .back-name__sub{font-size:24px}
</style>
</head>
<body>
  <section class="card card--front" aria-label="Card front">
    <div class="holder">
      <h1 class="holder__name">Daniel Hartley</h1>
      <p class="holder__title">Owner / Founder</p>
    </div>

    <ul class="contact">
      <li class="contact__row">
        <span class="contact__icon"><svg viewBox="0 0 16 16"><path d="M2 6c0-2 2-3 6-3s6 1 6 3l-2 1-1-2H5L4 7z M4 8h8l1 5H3z" fill="#fff"/></svg></span>
        <span class="contact__text">1.555.210.4830</span>
      </li>
      <li class="contact__row">
        <span class="contact__icon"><svg viewBox="0 0 16 16"><rect x="4" y="1" width="8" height="14" rx="1.5" fill="none" stroke="#fff" stroke-width="1.6"/></svg></span>
        <span class="contact__text">1.555.210.4871</span>
      </li>
      <li class="contact__row">
        <span class="contact__icon"><svg viewBox="0 0 16 16"><rect x="1.5" y="3.5" width="13" height="9" fill="none" stroke="#fff" stroke-width="1.4"/><path d="M1.5 3.5l6.5 5 6.5-5M1.5 12.5l5-4.5M14.5 12.5l-5-4.5" fill="none" stroke="#fff" stroke-width="1.2"/></svg></span>
        <span class="contact__text">daniel@ironvalehome.com</span>
      </li>
      <li class="contact__row">
        <span class="contact__icon"><svg viewBox="0 0 16 16"><path d="M8 15s-5-5.5-5-9a5 5 0 0 1 10 0c0 3.5-5 9-5 9z" fill="#fff"/><circle cx="8" cy="6" r="2" fill="#8e1a12"/></svg></span>
        <span class="contact__text">48 Harbor Lane, Westbrook, Maine</span>
      </li>
    </ul>

    <div class="brand">
      <span class="brand__mark" aria-hidden="true"></span>
      <p class="brand__name">Ironvale<br>Home Protection Inc.</p>
    </div>

    <div class="footer-band">
      <svg viewBox="0 0 700 56" preserveAspectRatio="none" aria-hidden="true">
        <rect x="0" y="8" width="700" height="48" fill="var(--gold)"/>
        <path d="M430 56 C445 20 455 8 490 8 L700 8 L700 56 Z" fill="var(--brand-red)"/>
        <rect x="0" y="8" width="430" height="3" fill="var(--gold-light)"/>
      </svg>
      <span class="footer-band__tagline">Residential &amp; Commercial Security Solutions</span>
      <span class="footer-band__web">www.ironvalehome.com</span>
    </div>
  </section>

  <section class="card card--back" aria-label="Card back">
    <p class="back-name">
      <span class="back-name__main">Ironvale</span><br>
      <span class="back-name__sub">Home Protection Inc.</span>
    </p>
  </section>
</body>
</html>
```